Website for new dental office

I am Dr. Colin Marsh and am building a new dental practice. I specialize in general dentistry. I am young and have a higher end dental practice incorporating very new technologies and would like my website to reflect that. As many dental patients are older, the website must be very easy to navigate. I would like patients to be able to request appointments, and will eventually add on patient information forms (the health history, etc, that you normally fill out in the practice) from my practice management software, so leave an area for that.

Industry/Entity Type

Building

```html
<!DOCTYPE html>
<html lang="en">
<head>
<meta charset="utf-8">
<title>Marsh Dental — Home</title>
<link rel="stylesheet" href="https://fonts.googleapis.com/css2?family=Cormorant+Garamond:wght@400;500&family=Raleway:wght@300;400&family=Arimo:wght@400&display=swap">
<style>
  :root {
    --navy: #2a2d3c;
    --navy-text: #1f2740;
    --white: #ffffff;
    --rule: #d9d9dc;
    --muted: #c9cbd3;
    --nav-text: #5a5d68;
    --photo-light: #f1efee;
    --photo-mid: #d9d3cf;
    --photo-warm: #e7cfc1;
  }
  * { margin: 0; padding: 0; box-sizing: border-box; }
  html, body { width: 1200px; height: 675px; overflow: hidden; background: var(--white); }
  .site { position: relative; width: 1200px; height: 675px; display: flex; }

  .sidebar {
    width: 102px; height: 100%; background: var(--white);
    border-right: 1px solid var(--rule);
    font-family: "Raleway", sans-serif;
  }
  .brand { height: 96px; padding-top: 22px; text-align: center; border-bottom: 1px solid var(--rule); }
  .brand-name { font-family: "Cormorant Garamond", serif; font-size: 15px; letter-spacing: 2px; color: var(--navy-text); }
  .brand-rule { width: 78px; margin: 4px auto; border-top: 1px solid var(--nav-text); }
  .brand-doctor { font-family: "Cormorant Garamond", serif; font-size: 10px; color: var(--nav-text); }
  .nav-list { list-style: none; }
  .nav-item {
    height: 48px; display: flex; align-items: center; justify-content: center;
    border-bottom: 1px solid var(--rule);
    font-size: 8px; letter-spacing: 1.2px; color: var(--nav-text); text-transform: uppercase; white-space: nowrap;
  }

  .main { flex: 1; display: flex; flex-direction: column; }
  .hero-intro {
    height: 270px; background: var(--navy); color: var(--muted);
    text-align: center; padding-top: 38px;
  }
  .practice-title { font-family: "Cormorant Garamond", serif; font-weight: 400; font-size: 25px; letter-spacing: 3px; color: var(--white); }
  .practice-title .region { font-size: 15px; letter-spacing: 2px; }
  .tagline { font-family: "Cormorant Garamond", serif; font-size: 13px; margin-top: 6px; color: var(--muted); }
  .intro-rule { width: 70px; margin: 20px auto 26px; border-top: 1px solid #6a6d7c; }
  .intro-copy { width: 380px; margin: 0 auto; font-family: "Raleway", sans-serif; font-weight: 300; font-size: 10.5px; line-height: 1.5; }

  .team-feature { position: relative; flex: 1; overflow: hidden; }
  .team-photo {
    position: absolute; inset: 0;
    background: linear-gradient(100deg, var(--photo-light) 0%, var(--photo-mid) 30%, var(--photo-light) 55%, var(--photo-warm) 78%, var(--photo-light) 100%);
  }
  .team-link { position: absolute; left: 400px; top: 168px; }
  .team-heading { font-family: "Arimo", sans-serif; font-size: 100px; line-height: 1; color: var(--navy-text); letter-spacing: -1px; }
  .team-cta { font-family: "Raleway", sans-serif; font-size: 12px; letter-spacing: 5px; color: var(--navy-text); margin-top: 2px; }
</style>
</head>
<body>
<div class="site">
  <aside class="sidebar">
    <div class="brand">
      <div class="brand-name">MARSH DENTAL</div>
      <div class="brand-rule"></div>
      <div class="brand-doctor">Colin Marsh, DDS</div>
    </div>
    <ul class="nav-list">
      <li class="nav-item">Services</li>
      <li class="nav-item">Team</li>
      <li class="nav-item">About</li>
      <li class="nav-item">Patient Resources</li>
      <li class="nav-item">Contact Us</li>
    </ul>
  </aside>

  <main class="main">
    <section class="hero-intro">
      <h1 class="practice-title">MARSH DENTAL, <span class="region">ORANGE COUNTY</span> CA.</h1>
      <p class="tagline">Specialists in general dentistry, cosmetics and more.</p>
      <div class="intro-rule"></div>
      <p class="intro-copy">Typically the home page includes an introductory blurb about practice philosophy, another page includes procedures we do-preventive, restorative, cosmetic, tooth replacement and some info on each, and there's normally a page about the dentist and staff, also location/contact information, and appointment request. I can also write up whatever is needed to make the site you create look good.</p>
    </section>

    <section class="team-feature">
      <div class="team-photo" role="img" aria-label="Photo of the dentist smiling in the foreground, with a dental assistant treating a patient under a dental lamp behind him"></div>
      <div class="team-link">
        <div class="team-heading">Dr Marsh</div>
        <div class="team-cta">Click here to meet our team</div>
      </div>
    </section>
  </main>
</div>
</body>
</html>
```